Trade Show Booth Sign Design for Retracting Banner

I need a trade show booth sign designed. It will be for a retractable banner that is double sided with 34 by 81 inch.

I want to incorporate my logo (see attached, have it in other file formats as well) and graphics from my website (https://www.pellacorvaadvisory.com/) with parts or all of the following text.

· Educational Content Creation
o Supplemental Textbook Content Development
o E-learning Content Development
· Curriculum Development
o VKTR/Joint Pillar
o Three Dimensional Learning
· Assessment
o Formative Assessments
o Elementary School, Middle School, High School, College, and Business
· Professional Development
o Training
o Facilitation

Target Market(s)

Education

Industry/Entity Type

Education

Font styles to use
Sans Serif

Colors

Designer to choose colors to be used in the design.

Requirements
Must have
• Eye catching and easy to read design
Nice to have
• Would like to see incorporation of my logo and some of the elements of my website images
Should not have
• N/A

```html
<!DOCTYPE html>
<html lang="en">
<head>
<meta charset="utf-8">
<title>Pellacorva Advisory – Retractable Banner</title>
<link rel="stylesheet" href="https://fonts.googleapis.com/css2?family=Archivo:wght@700;800&family=Arimo:wght@400&display=swap">
<style>
  :root {
    --navy: #0d2766;
    --white: #ffffff;
    --backdrop: #c9d0da;
    --chalk-dark: #2b2b2b;
    --chalk-mid: #454545;
    --orange: #f26b1d;
    --green: #3cb82e;
    --ring: #c8ccd2;
  }
  * { margin: 0; padding: 0; box-sizing: border-box; }
  html, body { width: 1200px; height: 1200px; overflow: hidden; }
  body { background: var(--backdrop); position: relative; }

  .banner {
    position: absolute;
    left: 360px; top: 30px;
    width: 495px; height: 1175px;
    transform: scale(0.97);
    transform-origin: top left;
    background: var(--white);
    overflow: hidden;
  }

  .brand {
    position: absolute; left: 0; top: 0; width: 100%; height: 172px;
    display: flex; flex-direction: column; align-items: center; justify-content: center;
    color: var(--navy);
    font-family: "Archivo", sans-serif; font-weight: 800;
    line-height: 1;
  }
  .brand__name { font-size: 56px; letter-spacing: 1px; }
  .brand__tag { font-size: 26px; letter-spacing: 6px; margin-top: 8px; }

  .hero {
    position: absolute; left: 0; top: 172px; width: 100%; height: 278px;
    background: radial-gradient(ellipse at 50% 55%, var(--chalk-mid), var(--chalk-dark));
  }

  .headline {
    position: absolute; left: 0; top: 405px; width: 430px; height: 88px;
    background: var(--navy); color: var(--white);
    font-family: "Arimo", sans-serif; font-weight: 400;
    font-size: 34px; line-height: 32px;
    padding: 12px 0 0 32px;
  }

  .service-icon {
    position: absolute; left: 27px; width: 142px; height: 142px;
    border-radius: 50%;
    background: var(--navy);
    border: 4px solid var(--ring);
  }
  .service-icon--content { top: 584px; }
  .service-icon--assess { top: 848px; }

  .service-list {
    position: absolute; left: 188px; list-style: none;
    font-family: "Archivo", sans-serif; font-weight: 700;
    font-size: 15.5px; line-height: 17px; color: var(--navy);
  }
  .service-list--content { top: 545px; }
  .service-list--assess { top: 820px; }
  .service-list li {
    position: relative; padding-left: 15px; margin-bottom: 17px;
  }
  .service-list li::before {
    content: ""; position: absolute; left: 0; top: 4px;
    width: 8px; height: 8px;
  }
  .service-list--content li::before { background: var(--orange); }
  .service-list--assess li::before { background: var(--green); }

  .footer {
    position: absolute; left: 0; bottom: 0; width: 100%; height: 52px;
    background: var(--navy); color: var(--white);
    font-family: "Archivo", sans-serif; font-weight: 700; font-size: 19px;
    display: flex; align-items: center; justify-content: center;
  }
</style>
</head>
<body>
  <main class="banner">
    <header class="brand">
      <span class="brand__name">PELLACORVA</span>
      <span class="brand__tag">ADVISORY</span>
    </header>

    <div class="hero" role="img" aria-label="Crumpled paper balls in red, blue, yellow, orange and light blue hanging like light bulbs against a dark chalkboard, the yellow one glowing with chalk rays"></div>

    <h1 class="headline">Research-Based<br>Educational Products</h1>

    <div class="service-icon service-icon--content" role="img" aria-label="Illustration of a teacher presenting charts on a board to a seated audience"></div>
    <ul class="service-list service-list--content">
      <li>Educational Content Creation</li>
      <li>Supplemental Textbook Content<br>Development</li>
      <li>E-learning Content Development</li>
      <li>Curriculum Development</li>
      <li>VKTR/Joint Pillar</li>
      <li>Three Dimensional Learning</li>
    </ul>

    <div class="service-icon service-icon--assess" role="img" aria-label="Illustration of a science flask surrounded by small education and science icons"></div>
    <ul class="service-list service-list--assess">
      <li>Assessment</li>
      <li>Formative Assessments</li>
      <li>Elementary School, Middle School,<br>High School, College, and Business</li>
      <li>Professional Development</li>
      <li>Training</li>
      <li>Facilitation</li>
    </ul>

    <footer class="footer">www.pellacorvaadvisory.com</footer>
  </main>
</body>
</html>
```